Banner for homepage

It is a new banner for the homepage, temporary site address is 203.0.113.57 ( is the biggest banner only ) . Would be 5 variations for image content as below (in Portuguese ) :

Image 1:
Leitor de codigo de barras
Todos os tipos de leitores de código de barras para as mais diversas aplicações.
( example of product images in : http://www.quorvelidx.com/en-US/Pages/Category.aspx?category=barcode-scanners&cat=QMT)

Image 2:
Impressora de etiquetas
Identifique o que for nessário com o melhor custo/beneficio e flexibilidade de materiais de impressão.
( example of product images in : tarnix.com in label printers desktop and industrial)

Image 3:
Impressora de cupom
Imprima recibos e cupons fiscais com agilidade e qualidade, temos a impressora certa para o seu PDV.
( example of product images in : http://www.plivorato.com.br/equipamento-categoria-impressoras+fiscais.html)

Image 4:
Coletor de dados
Computadores móveis com leitor de código de barras, que levam a automação para frente de trabalho.
( example of product images in : http://www.quorvelidx.com/en-US/Pages/Category.aspx?cat=QMT&category=hand-held-mobile-computer)

Image 5:
Etiquetas e Ribbons:
Etiquetas adesivas e não adesivas em vários de tipos de materiais, papéis e plásticos. O ribbon certo para impressão perfeita em cada material.
( example of product images in : http://www.lumetrask.com/cats/supplies/barcode-printer.htm?nav=hdr)

```html
<!DOCTYPE html>
<html lang="pt-BR">
<head>
<meta charset="utf-8">
<title>Brasquia – Soluções em Automação e Código de barras</title>
<link rel="stylesheet" href="https://fonts.googleapis.com/css2?family=Oswald:wght@400;500;600&family=Nunito:wght@800;900&family=Arimo:wght@400;700&display=swap">
<style>
  :root{
    --red:#c9323b;
    --red-dark:#a9232c;
    --page:#ebebeb;
    --nav:#3b3b3b;
    --nav-dark:#262626;
    --ink:#333;
    --white:#fff;
    --yellow:#ffd21a;
    --yellow-deep:#f5a300;
    --sky:#a9cbe6;
    --sky-light:#dbeaf6;
    --brown:#3a2d25;
    --taupe:#8c7b70;
    --tan:#d9b07a;
  }
  *{box-sizing:border-box;margin:0;padding:0}
  html,body{width:1200px;height:569px;overflow:hidden}
  body{background:var(--page);font-family:"Arimo",Arial,sans-serif;position:relative}
  .topbar{position:absolute;left:0;top:0;width:1200px;height:104px;background:linear-gradient(var(--red),var(--red-dark))}
  .brand{position:absolute;left:103px;top:8px;width:290px;height:45px;display:flex;align-items:center;gap:12px}
  .brand-dot{width:22px;height:22px;border-radius:50%;background:var(--white)}
  .brand-name{font-family:"Arimo",Arial,sans-serif;font-weight:700;font-size:30px;letter-spacing:3px;color:var(--white)}
  .tagline{position:absolute;left:119px;top:58px;color:var(--white);font-size:13px}
  .utility{position:absolute;right:108px;top:9px;display:flex;font-size:12px;font-weight:700;color:var(--white)}
  .utility span{padding:0 10px;border-left:1px solid rgba(255,255,255,.7)}
  .utility span:first-child{border-left:0}
  .utility span:last-child{padding-right:0}
  .contact-box{position:absolute;top:35px;height:47px;background:var(--white);border-radius:2px;padding:5px 11px;font-family:"Oswald",sans-serif}
  .contact-box b{display:block;font-weight:500;font-size:15px;color:var(--ink);line-height:20px}
  .contact-box small{display:block;font-size:11px;color:#e0452a;line-height:16px}
  .chat{left:824px;width:111px}
  .phones{left:952px;width:142px}
  .phones svg{position:absolute;right:10px;top:19px}
  .mainnav{position:absolute;left:75px;top:93px;width:1041px;height:42px;background:linear-gradient(#4a4a4a,var(--nav) 50%,var(--nav-dark));border-radius:4px;display:flex;align-items:center;padding-left:6px;box-shadow:0 1px 2px rgba(0,0,0,.4)}
  .mainnav a{font-family:"Oswald",sans-serif;font-size:12.5px;color:var(--white);text-decoration:none;padding:0 11px;line-height:42px;border-right:1px solid #555;text-transform:uppercase;letter-spacing:-.1px}
  .mainnav a:last-of-type{border-right:0}
  .search{position:absolute;right:11px;top:9px;width:150px;height:25px;background:#2c2c2c;border:1px solid #1c1c1c;border-radius:3px;color:#ddd;font-size:12px;padding:5px 8px}
  .search svg{position:absolute;right:6px;top:5px}
  .hero{position:absolute;left:97px;top:157px;width:743px;height:340px;border-radius:6px;overflow:hidden;box-shadow:0 1px 3px rgba(0,0,0,.3)}
  .hero-head{height:55px;background:linear-gradient(#555,#2f2f2f);text-align:center}
  .hero-title{font-family:"Oswald",sans-serif;font-weight:600;font-size:40px;line-height:55px;background:linear-gradient(#ffe86a,var(--yellow) 45%,var(--yellow-deep));-webkit-background-clip:text;background-clip:text;color:transparent}
  .hero-sky{height:200px;background:linear-gradient(var(--sky-light),var(--sky) 60%,#c6dcee)}
  .hero-copy{position:absolute;left:15px;top:76px;width:460px;padding:4px 0 10px;background:rgba(120,170,210,.35)}
  .hero-copy p{font-family:"Nunito",sans-serif;font-weight:900;font-size:26px;line-height:29px;color:var(--white);text-shadow:0 2px 0 #2d6f9f,0 0 3px #2d6f9f}
  .hero-base{height:85px;background:linear-gradient(#d8434b,var(--red-dark))}
  .hero-btn{position:absolute;left:108px;top:272px;width:212px;height:51px;border-radius:26px;background:linear-gradient(#ffe95e,var(--yellow) 50%,var(--yellow-deep));border:2px solid #c98a00;font-family:"Arimo",sans-serif;font-weight:700;font-size:32px;color:#3a2a00;text-align:center;line-height:47px}
  .hero-product{position:absolute;left:445px;top:66px;width:276px;height:255px;border-radius:14px;background:linear-gradient(160deg,#5a5e60,#2a2c2d)}
  .promo{position:absolute;left:864px;width:234px;height:162px;border-radius:4px;overflow:hidden;color:var(--white)}
  .promo-delivery{top:158px;background:linear-gradient(135deg,#4a3a30,var(--brown))}
  .promo-billing{top:336px;background:linear-gradient(135deg,#9a8a7f,var(--taupe))}
  .promo h2{position:absolute;left:24px;top:20px;font-family:"Oswald",sans-serif;font-weight:500;font-size:28px;line-height:34px;letter-spacing:-.3px}
  .promo-delivery h2 span{color:var(--tan)}
  .promo-billing h2 span{color:#3a3030}
  .promo p{position:absolute;left:24px;top:63px;font-size:12.5px;line-height:18px}
  .promo-billing p{left:29px}
  .promo-btn{position:absolute;left:23px;top:114px;width:92px;height:24px;border-radius:12px;font-size:12px;font-weight:700;text-align:center;line-height:24px}
  .promo-delivery .promo-btn{background:linear-gradient(#ecd1a3,#c09060);color:#4a2e14}
  .promo-billing .promo-btn{left:22px;top:96px;background:linear-gradient(#e5474f,#b12029)}
  .promo-art{position:absolute;right:0;bottom:0;width:88px;height:92px}
  .promo-delivery .promo-art{background:linear-gradient(#d58a47,#9a5524)}
  .promo-billing .promo-art{background:linear-gradient(#2b4a4a,#111)}
  .section-title{position:absolute;left:107px;top:528px;font-family:"Oswald",sans-serif;font-weight:500;font-size:18px;color:var(--ink)}
  .section-rule{position:absolute;left:97px;top:562px;width:1019px;height:2px;background:#ddd}
</style>
</head>
<body>
  <header class="topbar">
    <div class="brand"><span class="brand-dot"></span><span class="brand-name">BRASQUIA</span></div>
    <div class="tagline">Soluções em Automação e Código de barras</div>
    <nav class="utility"><span>Principal</span><span>Quem Somos</span><span>Entre em Contato</span></nav>
    <div class="contact-box chat"><b>CHAT ONLINE</b><small>CLIQUE AQUI</small></div>
    <div class="contact-box phones"><b>TELEFONES</b><small>TODOS OS ESTADOS</small>
      <svg width="9" height="5" viewBox="0 0 9 5"><path d="M0 0h9L4.5 5z" fill="#333"/></svg></div>
  </header>

  <nav class="mainnav">
    <a>Leitor de Código de Barras</a><a>Impressora de Etiquetas</a><a>Automação Comercial</a><a>Etiquetas</a><a>Coletor de Dados</a><a>Impressora de Cartão</a><a>Marcas</a>
    <div class="search">Busca
      <svg width="13" height="13" viewBox="0 0 13 13"><circle cx="5" cy="5" r="3.8" stroke="#fff" stroke-width="1.8" fill="none"/><path d="M8 8l4 4" stroke="#fff" stroke-width="2"/></svg></div>
  </nav>

  <section class="hero">
    <div class="hero-head"><h1 class="hero-title">IMPRESSORA DE CUPOM</h1></div>
    <div class="hero-sky"></div>
    <div class="hero-base"></div>
    <div class="hero-copy"><p>Imprima recibos e cupons fiscais<br>com agilidade e qualidade,<br>temos a impressora certa<br>para o seu PDV.</p></div>
    <div class="hero-product" role="img" aria-label="Foto de impressora de cupom fiscal térmica preta"></div>
    <div class="hero-btn">Veja Mais</div>
  </section>

  <aside class="promo promo-delivery">
    <h2><span>Entrega</span>Rápida</h2>
    <p>Enviamos sua compra<br>para todo o Brasil.</p>
    <div class="promo-art" role="img" aria-label="Ilustração de caixa de papelão para envio"></div>
    <div class="promo-btn">Leia Mais</div>
  </aside>
  <aside class="promo promo-billing">
    <h2><span>Boleto</span>Faturado</h2>
    <p>Receba seu pedido<br>com os boletos.</p>
    <div class="promo-art" role="img" aria-label="Ilustração de sacola de compras"></div>
    <div class="promo-btn">Leia Mais</div>
  </aside>

  <h3 class="section-title">DESTAQUES</h3>
  <div class="section-rule"></div>
</body>
</html>
```